Landing Page and Logo for Auto-Blogging Platform

I created a platform that allows users to start a blog for their business, hobby, charity, etc. I need a landing page where users can learn about the platform, benefits of consistent blogging, SEO value, plans/pricing, etc. The landing page needs to have multiple call to action buttons encouraging the visitor to register/sign up for a free trial.

In addition to the landing page, I need a page for users to establish the settings for their blog. This page should be a fairly simple form, intended for the user to enter a few details to set up their blog:
1. Name of Blog
2. Up to 10 topics and/or keywords the blog should focus on
3. Theme: Color-scheme and logo upload for blog.

I have attached the specifications of the platform's functionality so you can better understand how it works, plans/pricing, etc.

I also need a logo for the business. The name of the platform is PennaWave.

Target Market(s)

Website owners, bloggers, business owners

Industry/Entity Type

Technology, Internet, web design

Coding

Coded - Design and coding required

Number of Pages Required

2 page

Colors
0054AA
0677BA
7BADD7
CADEEF
E8F1F8
0094D4
00A9DD
6FCCEA
C7EBF8
E9F6FB

Requirements
Must have
• Eye-catching design but fairly light on content (keep it simple and brief.)
Nice to have
• Eye-catching yet simple design, clean and easy to understand what we are offering.
Should not have
• Too much “wordy” and confusing content.

```html
<!DOCTYPE html>
<html lang="en">
<head>
<meta charset="utf-8">
<title>PennaWave — Automate Your Blog Posting With AI</title>
<link href="https://fonts.googleapis.com/css2?family=Montserrat:wght@300;400;500;600;700&display=swap" rel="stylesheet">
<style>
:root{
  --navy:#0054AA;
  --blue:#0677BA;
  --sky:#0094D4;
  --cyan:#00A9DD;
  --soft:#7BADD7;
  --pale:#E8F1F8;
  --ice:#E9F6FB;
  --ink:#1a1a1a;
  --text:#444;
  --white:#fff;
}
*{margin:0;padding:0;box-sizing:border-box}
html,body{width:1200px;height:5034px;overflow:hidden}
body{font-family:'Montserrat',sans-serif;color:var(--text);background:var(--white);position:relative}
section,header,footer{position:absolute;left:0;width:1200px}
.abs{position:absolute}
.btn{position:absolute;display:flex;align-items:center;justify-content:center;border-radius:40px;color:var(--white);font-weight:600;text-transform:uppercase;background:var(--sky);white-space:nowrap}
.rule{position:absolute;height:3px;width:47px;background:var(--navy)}
h2{position:absolute;font-weight:700;color:var(--ink);font-size:30px;text-transform:uppercase;letter-spacing:-.3px}
.photo{position:absolute}

/* header */
.site-header{top:0;height:111px}
.brand{position:absolute;display:flex;align-items:center;gap:12px;font-weight:600;color:var(--navy)}
.brand .mark{width:44px;height:44px;background:var(--navy);border-radius:8px}
.site-header .brand{left:129px;top:33px;font-size:24px}
.nav a{position:absolute;top:47px;font-size:13px;font-weight:500;color:var(--ink);text-decoration:none}
.nav a.active{color:var(--sky)}
.nav a.active::after{content:"";position:absolute;left:2px;right:2px;bottom:-12px;height:3px;background:var(--sky)}

/* hero */
.hero{top:111px;height:602px}
.hero .photo{inset:0;background:linear-gradient(100deg,#8a5a34 0%,#b07a4c 35%,#c99a6a 60%,#d8c2a6 80%,#a37650 100%)}
.hero h1{position:absolute;left:119px;top:76px;color:var(--white);font-size:54px;line-height:62px;font-weight:400;text-transform:uppercase}
.hero h1 b{font-weight:700}
.hero p{position:absolute;left:122px;top:286px;width:400px;color:var(--white);font-size:15px;line-height:21px;font-weight:400}
.dots{position:absolute;left:562px;top:547px;display:flex;gap:12px}
.dots i{width:10px;height:10px;border-radius:50%;background:var(--white)}
.dots i:first-child{background:var(--sky)}

/* plans */
.plans{top:713px;height:665px}
.plan{position:absolute;top:244px;width:291px;height:333px;background:var(--white);border-radius:50% 50% 8px 8px / 40px 40px 8px 8px;box-shadow:0 6px 24px rgba(0,60,120,.12);text-align:center;color:var(--ink)}
.plan.featured{background:var(--sky);color:var(--white)}
.plan .badge{position:absolute;left:50%;top:-46px;margin-left:-33px;width:66px;height:66px;border-radius:50%;background:var(--navy);display:flex;align-items:center;justify-content:center}
.plan.featured .badge{background:var(--sky);border:4px solid var(--white)}
.price{position:absolute;top:48px;width:100%;font-size:30px;font-weight:700;color:var(--navy)}
.price sup{font-size:15px;vertical-align:14px}
.price small{font-size:14px;font-weight:500}
.plan.featured .price{color:var(--white)}
.plan h3{position:absolute;top:108px;width:100%;font-size:19px;font-weight:500;text-transform:uppercase}
.plan .line1{position:absolute;top:142px;width:100%;font-size:14px}
.plan .line2{position:absolute;top:177px;width:100%;font-size:14px}
.plan .freq{position:absolute;top:212px;left:50%;transform:translateX(-50%);border:1.5px solid var(--navy);border-radius:20px;padding:6px 14px;font-size:13px;color:var(--navy);white-space:nowrap;background:var(--white)}
.plan .btn{top:266px;left:50%;transform:translateX(-50%);width:94px;height:34px;font-size:12px}
.plan.featured .btn{background:var(--navy)}

/* about */
.about{top:1378px;height:586px;background:var(--pale)}
.about .photo{left:0;top:0;width:629px;height:586px;background:linear-gradient(135deg,#3e5a3a 0%,#7f8d6a 35%,#c9c4b5 60%,#a08866 100%)}
.about p,.seo p{position:absolute;font-size:13.5px;line-height:19.5px}

/* benefits */
.benefits{top:1964px;height:1084px}
.card{position:absolute;width:219px;height:338px;background:var(--white);box-shadow:0 4px 22px rgba(0,60,120,.1);text-align:center}
.card svg{position:absolute;left:50%;top:36px;transform:translateX(-50%)}
.card h4{position:absolute;top:120px;width:100%;font-size:15px;font-weight:500;line-height:24px;color:var(--ink)}
.card .bar{position:absolute;top:182px;left:50%;margin-left:-13px;width:26px;height:2px;background:var(--cyan)}
.card p{position:absolute;top:212px;left:22px;right:22px;font-size:12px;line-height:19px}

/* seo */
.seo{top:3048px;height:551px}
.seo .photo{inset:0;background:linear-gradient(90deg,#5c6f82 0%,#8799ab 30%,#cfd8e0 55%,#f2f4f6 68%,#f7f8f9 100%)}

/* setup */
.setup{top:3599px;height:749px}
.setup .photo{left:549px;top:65px;width:516px;height:606px;background:linear-gradient(150deg,#5b4330 0%,#8c6c4c 40%,#bfb9b0 60%,#6c5440 100%)}
.step-line{position:absolute;left:161px;width:2px;background:var(--navy)}
.step-icon{position:absolute;left:127px;width:70px;height:70px;border-radius:50%;background:var(--sky);border:5px solid #bfe6f6;display:flex;align-items:center;justify-content:center}
.step-tag{position:absolute;left:221px;background:var(--navy);color:var(--white);font-size:14px;font-weight:600;padding:2px 6px}
.step-text{position:absolute;left:225px;width:290px;font-size:15px;line-height:24px;color:var(--ink)}

/* cta */
.cta{top:4348px;height:312px;background:var(--navy);text-align:center;color:var(--white)}
.cta h2{color:var(--white);width:100%;top:70px;font-size:32px}
.cta p{position:absolute;width:100%;top:128px;font-size:19px}

/* footer */
.site-footer{top:4660px;height:374px}
.site-footer .brand{left:129px;top:110px;font-size:24px}
.col{position:absolute;top:46px;font-size:12px;color:var(--text)}
.col h5{font-size:12px;font-weight:600;color:var(--ink);margin-bottom:18px}
.col li{list-style:none;line-height:27px}
.socials{position:absolute;left:898px;top:82px;display:flex;gap:5px}
.socials i{width:36px;height:36px;border-radius:50%;border:2px solid var(--navy)}
.footer-rule{position:absolute;left:129px;top:280px;width:940px;height:1px;background:var(--navy)}
.copy{position:absolute;top:322px;width:100%;text-align:center;font-size:12px}
</style>
</head>
<body>

<header class="site-header">
  <div class="brand"><span class="mark"></span>PennaWave</div>
  <nav class="nav">
    <a href="#" class="active" style="left:346px">HOME</a>
    <a href="#" style="left:408px">ABOUT US</a>
    <a href="#" style="left:504px">BENEFITS</a>
    <a href="#" style="left:592px">CONTACT US</a>
  </nav>
  <a class="btn" style="left:705px;top:36px;width:155px;height:38px;font-size:12px;background:var(--navy)">Create your blog</a>
  <a class="btn" style="left:870px;top:36px;width:199px;height:38px;font-size:12px;background:var(--cyan)">Sign up for a free trial</a>
</header>

<section class="hero">
  <div class="photo" role="img" aria-label="Hands typing on a laptop on a wooden desk, the screen showing a blog home page"></div>
  <h1><b>Automate</b><br>your blog<br>posting with AI</h1>
  <p>Transform your blogging experience with our AI-powered platform that not only generates and optimizes content tailored to your audience but also continuously learns and adapts to deliver smarter insights, ensuring your voice stands out in a crowded digital landscape.</p>
  <a class="btn" style="left:121px;top:440px;width:282px;height:55px;font-size:16px;background:var(--cyan)">Sign up for a free trial</a>
  <div class="dots"><i></i><i></i><i></i><i></i></div>
</section>

<section class="plans">
  <h2 style="left:0;width:1200px;text-align:center;top:68px">Our Plans</h2>
  <div class="rule" style="left:577px;top:137px"></div>

  <div class="plan" style="left:135px">
    <div class="badge"><svg width="30" height="30" viewBox="0 0 30 30" fill="none" stroke="#fff" stroke-width="2"><rect x="6" y="4" width="18" height="22" rx="2"/><path d="M18 10h-4a2 2 0 0 0 0 4h2a2 2 0 0 1 0 4h-4M15 8v12"/></svg></div>
    <div class="price">$9.<sup>99</sup><small>/mo</small></div>
    <h3>Base Plan</h3>
    <div class="line1">1 blog post</div>
    <div class="line2">(up to 2,000 words)</div>
    <div class="freq">every month</div>
    <a class="btn">Sign up</a>
  </div>

  <div class="plan featured" style="left:453px">
    <div class="badge"><svg width="30" height="30" viewBox="0 0 30 30" fill="none" stroke="#fff" stroke-width="2"><path d="M8 6h14l5 7-12 13L3 13z M3 13h24 M15 26 11 13l4-7 4 7z"/></svg></div>
    <div class="price">$9.<sup>99</sup><small>/mo</small></div>
    <h3>Premium Plan</h3>
    <div class="line1">1 blog post</div>
    <div class="line2">(up to 2,000 words)</div>
    <div class="freq">every week</div>
    <a class="btn">Sign up</a>
  </div>

  <div class="plan" style="left:778px">
    <div class="badge"><svg width="30" height="30" viewBox="0 0 30 30" fill="none" stroke="#fff" stroke-width="2"><rect x="5" y="13" width="20" height="13"/><path d="M3 9h24v4H3z M15 9v17 M15 9c-3-5-8-4-6 0 M15 9c3-5 8-4 6 0"/></svg></div>
    <div class="price">$24.<sup>99</sup><small>/mo</small></div>
    <h3>Ultimate Plan</h3>
    <div class="line1">1 blog post</div>
    <div class="line2">(up to 3,000 words)</div>
    <div class="freq">per day plus unlimited manual posting</div>
    <a class="btn">Sign up</a>
  </div>
</section>

<section class="about">
  <div class="photo" role="img" aria-label="Desktop computer on a wooden desk showing the blog dashboard, with keyboard and mouse"></div>
  <h2 style="left:684px;top:68px">About the Platform</h2>
  <div class="rule" style="left:684px;top:130px"></div>
  <p style="left:686px;top:168px;width:370px">Each user will have a dashboard where they control their settings such as account information, billing, view blog posts, view blog post topics, etc. From this dashboard, the user can customize the "look and feel" of their blog including theme, hero banner, header, footer, logo, color scheme, etc.</p>
  <p style="left:686px;top:304px;width:370px">The platform will require a list of blog topics. Based on the topics list, the software will need to automatically send prompts to TextGenie in the specified intervals (monthly, weekly, or daily), receive the blog content, and post it to the blog. Furthermore, the software will need some method of adding at least one image to each blog post.</p>
  <a class="btn" style="left:690px;top:474px;width:113px;height:36px;font-size:12px;background:var(--sky)">Read more</a>
</section>

<section class="benefits">
  <h2 style="left:0;width:1200px;text-align:center;top:74px">Benefits</h2>
  <div class="rule" style="left:577px;top:141px"></div>

  <div class="card" style="left:129px;top:209px">
    <svg width="52" height="52" viewBox="0 0 52 52" fill="none" stroke="#0054AA" stroke-width="2.5"><rect x="4" y="6" width="36" height="30"/><path d="M4 13h36M10 20h14M10 26h10"/><circle cx="34" cy="34" r="9" fill="#fff"/><path d="M41 41l8 8"/></svg>
    <h4>Boost Your<br>SEO Rankings</h4><div class="bar"></div>
    <p>Consistent blogging is one of the most effective ways to improve your website's search engine ranking.</p>
  </div>
  <div class="card" style="left:369px;top:209px">
    <svg width="52" height="52" viewBox="0 0 52 52" fill="none" stroke="#0054AA" stroke-width="2.5"><rect x="9" y="4" width="28" height="38" fill="#0054AA"/><path d="M15 14h16M15 20h16M15 26h10" stroke="#fff"/><circle cx="38" cy="38" r="9" fill="#fff"/></svg>
    <h4>Build Authority<br>and Trust</h4><div class="bar"></div>
    <p>When you consistently share valuable insights, tips, and information on your blog, you establish yourself as an authority in your industry.</p>
  </div>
  <div class="card" style="left:610px;top:209px">
    <svg width="52" height="52" viewBox="0 0 52 52" fill="none" stroke="#0054AA" stroke-width="2.5"><rect x="4" y="6" width="44" height="40"/><path d="M4 13h44"/><path d="M14 38v-8M22 38v-12M30 38v-6M38 38v-14" stroke="#0094D4" stroke-width="4"/></svg>
    <h4>Drive More Traffic<br>to Your Website</h4><div class="bar"></div>
    <p>Each new blog post is a new page on your website, and each page is another opportunity to attract visitors.</p>
  </div>
  <div class="card" style="left:850px;top:209px">
    <svg width="52" height="52" viewBox="0 0 52 52" fill="#0054AA"><path d="M8 4h36v5H8zM12 12h28v5H12zM16 20h20v5H16z"/><circle cx="26" cy="38" r="10" fill="#0094D4"/></svg>
    <h4>Generate Leads and<br>Nurture Relationships</h4><div class="bar"></div>
    <p>Blogging allows you to provide content that resonates with your target audience, helping you to capture</p>
  </div>

  <div class="card" style="left:129px;top:566px">
    <svg width="52" height="52" viewBox="0 0 52 52" fill="none" stroke="#0054AA" stroke-width="2.5"><path d="M6 20h8l20-12v36L14 32H6z" fill="#0054AA"/><path d="M14 32l4 12h6l-3-12M40 18c4 4 4 12 0 16"/></svg>
    <h4>Enhance Your<br>Brand Voice</h4><div class="bar"></div>
    <p>Consistent blogging is one of the most effective ways to improve your website's search engine ranking.</p>
  </div>
  <div class="card" style="left:369px;top:566px">
    <svg width="52" height="52" viewBox="0 0 52 52" fill="#0054AA"><rect x="6" y="8" width="18" height="18"/><rect x="28" y="26" width="18" height="18" fill="#0094D4"/><rect x="10" y="30" width="14" height="14"/><circle cx="38" cy="14" r="7" fill="#0094D4"/></svg>
    <h4>Support Your<br>Social Media Strategy</h4><div class="bar"></div>
    <p>When you consistently share valuable insights, tips, and information on your blog, you establish yourself as an authority in your industry.</p>
  </div>
  <div class="card" style="left:610px;top:566px">
    <svg width="52" height="52" viewBox="0 0 52 52" fill="#0054AA"><circle cx="26" cy="8" r="5"/><circle cx="12" cy="14" r="5"/><circle cx="40" cy="14" r="5"/><path d="M6 24h12l-3 22H9zM20 20h12l-3 26h-6zM34 24h12l-3 22h-6z"/></svg>
    <h4>Educate and Engage<br>Your Audience</h4><div class="bar"></div>
    <p>Each new blog post is a new page on your website, and each page is another opportunity to attract visitors.</p>
  </div>
  <div class="card" style="left:850px;top:566px">
    <svg width="52" height="52" viewBox="0 0 52 52" fill="#0054AA"><path d="M14 4a10 10 0 1 0 10 10H14z" fill="#0094D4"/><path d="M28 6h18v3H28zM28 13h14v3H28zM28 20h18v3H28z"/><path d="M6 46h4v-6H6zM13 46h4v-10h-4zM20 46h4v-8h-4zM27 46h4v-14h-4zM34 46h4v-10h-4zM41 46h4v-16h-4z"/></svg>
    <h4>Achieve<br>Long-Term Results</h4><div class="bar"></div>
    <p>Blogging allows you to provide content that resonates with your target audience, helping you to capture</p>
  </div>

  <a class="btn" style="left:457px;top:960px;width:286px;height:56px;font-size:16px;background:var(--cyan)">Sign up for a free trial</a>
</section>

<section class="seo">
  <div class="photo" role="img" aria-label="Smiling man holding a tablet in a bright office, with a search bar floating in front of him"></div>
  <h2 style="left:731px;top:100px">SEO Value</h2>
  <div class="rule" style="left:731px;top:158px"></div>
  <p style="left:731px;top:207px;width:350px">Sed ut perspiciatis unde omnis iste natus error sit voluptatem accusantium doloremque laudantium, totam rem aperiam, eaque ipsa quae ab illo inventore veritatis et quasi architecto beatae vitae dicta sunt explicabo. Nemo enim ipsam voluptatem quia voluptas sit aspernatur aut odit aut fugit , sed quia consequuntur magni dolores eos qui ratione voluptatem sequi nesciunt. Neque porro quisquam est, qui dolorem ipsum quia</p>
  <a class="btn" style="left:731px;top:400px;width:116px;height:36px;font-size:12px;background:var(--sky)">Read more</a>
</section>

<section class="setup">
  <h2 style="left:133px;top:72px;font-size:32px;line-height:42px">How to set up<br>the auto-blog</h2>
  <div class="rule" style="left:135px;top:164px"></div>

  <div class="step-line" style="top:286px;height:46px"></div>
  <div class="step-line" style="top:403px;height:46px"></div>
  <div class="step-line" style="top:520px;height:48px"></div>

  <div class="step-icon" style="top:216px"><svg width="30" height="30" viewBox="0 0 30 30" fill="none" stroke="#fff" stroke-width="2"><rect x="4" y="5" width="20" height="20"/><path d="M4 10h20M9 15h10M9 19h6"/><circle cx="23" cy="23" r="5" fill="#0094D4"/></svg></div>
  <div class="step-tag" style="top:223px">Step 1</div>
  <div class="step-text" style="top:248px">Select frequency of Automated Blog Posts (daily, weekly, or monthly)</div>

  <div class="step-icon" style="top:333px"><svg width="30" height="30" viewBox="0 0 30 30" fill="none" stroke="#fff" stroke-width="2"><rect x="4" y="5" width="22" height="20"/><path d="M4 10h22M9 14h12M9 18h12M9 22h8"/></svg></div>
  <div class="step-tag" style="top:352px">Step 2</div>
  <div class="step-text" style="top:379px">Name your blog</div>

  <div class="step-icon" style="top:450px"><svg width="30" height="30" viewBox="0 0 30 30" fill="none" stroke="#fff" stroke-width="2"><rect x="4" y="5" width="22" height="20"/><path d="M4 10h22M8 14h6v7H8zM17 14h5M17 18h5M17 22h5"/></svg></div>
  <div class="step-tag" style="top:460px">Step 3</div>
  <div class="step-text" style="top:486px">Select your blog topics (or let AI choose them for you)</div>

  <div class="step-icon" style="top:570px"><svg width="30" height="30" viewBox="0 0 30 30" fill="none" stroke="#fff" stroke-width="2"><path d="M8 26v-6a9 9 0 1 1 12 0v6z"/><rect x="11" y="10" width="8" height="6"/></svg></div>
  <div class="step-tag" style="top:578px">Step 4</div>
  <div class="step-text" style="top:605px">Go do something else and let AI do all your blogging for you!</div>

  <div class="photo" role="img" aria-label="Hands typing on a laptop showing a blog page, next to a calculator and newspaper on a wooden desk"></div>
</section>

<section class="cta">
  <h2>Create your free online blog</h2>
  <p>No fees. No catch. In just a few clicks.</p>
  <a class="btn" style="left:457px;top:182px;width:286px;height:56px;font-size:16px;background:var(--cyan)">Sign up for a free trial</a>
</section>

<footer class="site-footer">
  <div class="brand"><span class="mark"></span>PennaWave</div>
  <div class="col" style="left:352px"><h5>LINKS</h5><ul><li>Build your website or blog</li><li>Create a business website</li><li>Templates</li><li>Features</li><li>Website Premium Plans</li><li>Partners &amp; Integrations</li></ul></div>
  <div class="col" style="left:586px"><h5>FOLLOW US</h5><ul><li>Circlebook</li><li>Chirpline</li><li>ViewStream</li><li>Snapgrid</li></ul></div>
  <div class="col" style="left:756px"><h5>MENU</h5><ul><li>Home</li><li>About us</li><li>Benefits</li><li>Contact us</li></ul></div>
  <div class="col" style="left:901px"><h5>FOLLOW US</h5></div>
  <div class="socials"><i></i><i></i><i></i><i></i></div>
  <div class="footer-rule"></div>
  <div class="copy">Copyright © 2024 All Rights Reserved</div>
</footer>

</body>
</html>
```